We need a .psd design for a store we are creating called Bright Pouches. I will need only the main home page designed.

The store will be an eCommerce website that sells custom printed men's wallets. Customers will come onto the website and be able to upload their own images or add text to the front, back and inside of the wallet. We will initially be launching with one wallet style and will be expanding our range in the future for now the only images of a wallet on the website should be of the style attached.

There will be multiple templates that a customer can choose and edit the design of so there will effectively be a large number of products on display in the store. However, on the homepage there should just be a couple of featured products and the main emphasis should be on the features of the wallet/website and links to other areas of the website (customise your own wallet, edit our templates, bespoke designer wallets).

For the styling of the website, it needs to be funky and fresh with lots of colour. The logo of the website is attached and the styling should mirror the logo style.

The main features of the website should be on the home page. These features are:
- 5 year money back guarantee on wallet
- High quality, durable leather, made to last
- customer can upload photo and edit them online with our online picture editor
- 3d mockup of the wallet as you are designing it to show what it looks like with custom images on
- Edit any of our ready made wallet designs

Features of this wallet may be used as well - these can be viewed on "Image 6" of the attached product image .psd files.

Attached are the logo for the website and the wallet product photos. The product photos are provided in .psd format and have smart objects so that you can add any image to the front/inside of the wallets for any images on the website you create. Fee free to edit them and use them for banner images and feature images however you feel necessary.

The term "what does you wallet say about you" should be used as this is a tagline for most of the marketing - based on the fact that the wallets are personalised to each individual they will show off that individuals personality and what they like.

The eventual website will be hosted on cartnest and will more than likely use the "StallKit" theme. This is a highly adaptable theme and examples of the layout styles for the homepage can be found here: http://reef.lindolayouts.example/cartnest/stallkit-intro/?storefront=pixora-assets however i do not want you to just copy a ready made template and stick some stock photos in - I only want one page designing here, put the effort in with the banners and feature images and you'll win this.

Any images that you create for hero sliders/banners should be provided in .psd format so that they can be edited as necessary in the future. A newsletter popup should also be designed as the website will have postwren integration, the newsletter popup is a 500 x 750 image that pops up with a message saying "subscribe to our newsletter and get 10% off your next order".

There should also be an area of the page that has customer testimonials.

Target Market(s)

Males, aged 18 - 45

Industry/Entity Type

Retail

Number of Pages Required

1 page

Font styles to use
Serif
Decorative
Script

Colors

Designer to choose colors to be used in the design.

Requirements
Must have
• Vibrant and uplifting feel to the website
• Design which reflects the logo
• Features of the website and wallets should feature prominently on the homepage (but not in banner/hero image)
Nice to have
• hipster/geek/easygoing vibe
• Images that have used the wallet .psd files and have different designs on them showing customers that anything can be printed on the wallets
• Custom images/styles for the featured images and main banner.
Should not have
• - Boring images
• - Stock Photos
• - Mundane feel
• - Square block style images - try putting images in circles or geometric shapes with colours, just adding a stock photo to some "lorem Ipsum" text will not win you this contest

```html
<!DOCTYPE html>
<html lang="en">
<head>
<meta charset="utf-8">
<title>Bright Pouches — Home</title>
<link rel="stylesheet" href="https://fonts.googleapis.com/css2?family=Fredoka:wght@500;600;700&family=Comfortaa:wght@400;700&display=swap">
<style>
:root{
  --white:#ffffff;
  --ink:#1d1d24;
  --orange:#f7941d;
  --yellow:#ffd200;
  --magenta:#e6197e;
  --purple:#5b2a9e;
  --violet:#7b2ff0;
  --teal:#14b8b0;
  --green:#7ed321;
  --blue:#1e88e5;
  --footer:#2a2a2d;
  --head:"Fredoka", sans-serif;
  --body:"Comfortaa", sans-serif;
}
*{box-sizing:border-box;margin:0;padding:0}
html,body{width:1200px;height:4082px;overflow:hidden}
body{font-family:var(--body);color:var(--white);position:relative;background:var(--ink)}
section,footer{position:absolute;left:0;width:1200px;overflow:hidden}
.abs{position:absolute}
.section-title{position:absolute;left:0;width:1200px;text-align:center;font-family:var(--head);font-weight:600;font-size:48px;letter-spacing:1px}
.btn{position:absolute;display:flex;align-items:center;justify-content:center;background:var(--white);border-radius:30px;font-family:var(--head);font-weight:600;font-size:22px;text-decoration:none}
.media{position:absolute;border-radius:12px}

/* Hero */
.hero{top:0;height:686px;background:
  radial-gradient(circle at 90% 20%,#ffb400 0,transparent 28%),
  radial-gradient(circle at 10% 15%,#00c6d8 0,transparent 30%),
  radial-gradient(circle at 85% 75%,#ffc400 0,transparent 25%),
  radial-gradient(circle at 30% 85%,#e0218a 0,transparent 35%),
  linear-gradient(115deg,#3b5bdb 0%,#7b2ff0 35%,#c22bb8 60%,#f26b3a 100%)}
.main-nav{position:absolute;top:38px;left:0;width:1200px;height:30px;font-size:17px;font-weight:700}
.main-nav a{position:absolute;color:var(--white);text-decoration:none;transform:translateX(-50%)}
.brand{position:absolute;top:130px;left:600px;transform:translateX(-50%);display:flex;align-items:center;gap:12px;font-family:var(--head);font-weight:600;font-size:40px;white-space:nowrap}
.brand-dot{width:22px;height:22px;border-radius:50%;background:var(--white)}
.hero-wallet{left:155px;top:218px;width:545px;height:296px;background:linear-gradient(135deg,#f2f2f2 0%,#3a3a3a 45%,#bdbdbd 100%)}
.hero-title{position:absolute;left:721px;top:252px;width:292px;text-align:center;font-family:var(--head);font-weight:600;font-size:46px;line-height:53px}
.hero-sub{position:absolute;left:0;top:538px;width:1200px;text-align:center;font-size:19px}
.hero .btn{left:471px;top:598px;width:270px;height:55px;color:var(--orange)}

/* About */
.about{top:686px;height:511px;background:
  radial-gradient(circle at 15% 30%,#ffd000 0,transparent 35%),
  radial-gradient(circle at 80% 80%,#ffe14d 0,transparent 35%),
  linear-gradient(180deg,#f7a21b 0%,#f9c21a 60%,#fbd12b 100%)}
.about .section-title{top:84px}
.perk{position:absolute;top:180px;width:240px;transform:translateX(-50%);text-align:center}
.perk-badge{width:170px;height:170px;margin:0 auto;border-radius:50%;background:radial-gradient(circle,#e9771b 0 55%,#d9811f 56% 64%,transparent 65%);display:flex;align-items:center;justify-content:center}
.perk-text{width:180px;margin:34px auto 0;font-size:15px;line-height:22px;font-weight:700}

/* Features */
.features{top:1197px;height:686px;background:
  radial-gradient(circle at 10% 20%,#ff3d8b 0,transparent 35%),
  radial-gradient(circle at 88% 30%,#c2185b 0,transparent 35%),
  radial-gradient(circle at 70% 90%,#ff9800 0,transparent 30%),
  linear-gradient(120deg,#e91e63 0%,#b0126a 45%,#7b1fa2 75%,#e65100 100%)}
.features .section-title{top:88px}
.feature-wallet{left:440px;top:198px;width:320px;height:230px;background:radial-gradient(circle,#2b2b2b 0 45%,#f3d9ee 70%,transparent 72%);border-radius:50%}
.spec{position:absolute;font-size:15px;line-height:22px;font-weight:700;display:flex;align-items:flex-start;gap:12px}
.spec-dot{flex:none;width:16px;height:16px;border-radius:50%;border:3px solid var(--white);margin-top:3px}
.spec.right{flex-direction:row-reverse;text-align:right}
.detail{position:absolute;top:1725px;width:130px;height:130px;border-radius:50%;border:6px solid;background:linear-gradient(135deg,#555,#1a1a1a)}

/* Products */
.products{top:1883px;height:688px;background:
  radial-gradient(circle at 15% 20%,#00bcd4 0,transparent 35%),
  radial-gradient(circle at 85% 25%,#26c6da 0,transparent 30%),
  radial-gradient(circle at 20% 85%,#c6ff00 0,transparent 35%),
  radial-gradient(circle at 85% 85%,#00e5ff 0,transparent 30%),
  linear-gradient(160deg,#19b5c9 0%,#6fd36a 50%,#d7e91c 75%,#2fc7c1 100%)}
.products .section-title{top:120px}
.products-intro{position:absolute;left:205px;top:210px;width:790px;text-align:center;font-size:15px;line-height:24px}
.product{position:absolute;top:315px;width:280px;text-align:center}
.product-shot{height:191px;border-radius:10px}
.product-name{margin-top:36px;font-size:15px;font-weight:700}
.product-price{margin-top:10px;font-size:14px;font-weight:700}
.products .btn{left:490px;top:604px;width:220px;height:51px;color:var(--teal)}

/* Edit templates */
.templates{top:2571px;height:688px;background:
  radial-gradient(circle at 15% 15%,#ffc107 0,transparent 28%),
  radial-gradient(circle at 80% 15%,#c2185b 0,transparent 30%),
  radial-gradient(circle at 25% 70%,#ff5722 0,transparent 30%),
  linear-gradient(140deg,#e8701a 0%,#9c27b0 45%,#4a148c 80%,#311b92 100%)}
.templates-screen{left:120px;top:90px;width:520px;height:420px;background:linear-gradient(160deg,#3a3a44,#1c1c22)}
.templates .title{position:absolute;left:660px;top:86px;width:370px;text-align:right;font-family:var(--head);font-weight:600;font-size:48px}
.templates .copy{position:absolute;left:640px;top:262px;width:388px;text-align:right;font-size:15px;line-height:24px}
.templates .copy p+p{margin-top:14px}
.templates .btn{left:805px;top:454px;width:221px;height:51px;color:var(--magenta)}

/* Customize */
.customize{top:3259px;height:681px;background:
  radial-gradient(circle at 85% 15%,#00b0ff 0,transparent 30%),
  radial-gradient(circle at 15% 80%,#2979ff 0,transparent 35%),
  radial-gradient(circle at 70% 85%,#00e5ff 0,transparent 28%),
  linear-gradient(170deg,#1e9be0 0%,#1f6fd6 50%,#2b4fc4 100%)}
.customize .title{position:absolute;left:171px;top:80px;width:420px;font-family:var(--head);font-weight:600;font-size:48px;line-height:72px}
.customize .copy{position:absolute;left:171px;top:288px;width:360px;font-size:15px;line-height:24px}
.customize .copy p+p{margin-top:14px}
.customize .btn{left:171px;top:468px;width:221px;height:55px;color:var(--blue)}
.customize-screen{left:560px;top:145px;width:515px;height:430px;background:linear-gradient(160deg,#2f2f36,#141418)}

.site-footer{top:3940px;height:142px;background:var(--footer)}
</style>
</head>
<body>

<section class="hero">
  <nav class="main-nav">
    <a style="left:226px">About</a>
    <a style="left:337px">Features</a>
    <a style="left:460px">Products</a>
    <a style="left:735px">Contact</a>
    <a style="left:865px">Templates</a>
    <a style="left:1007px">Customize</a>
  </nav>
  <div class="brand"><span class="brand-dot"></span>Bright Pouches</div>
  <div class="media hero-wallet abs" role="img" aria-label="Custom printed wallet opened beside its colourful gift box"></div>
  <h1 class="hero-title">What does your wallet say about you?</h1>
  <p class="hero-sub">Create a wallet that reflects your inner being.</p>
  <a class="btn">Get Started</a>
</section>

<section class="about">
  <h2 class="section-title">About</h2>
  <div class="perk" style="left:253px">
    <div class="perk-badge"><svg width="80" height="80" viewBox="0 0 80 80"><circle cx="40" cy="40" r="36" fill="#fff"/><path d="M24 41l11 11 22-24" fill="none" stroke="#f0a020" stroke-width="8" stroke-linecap="round" stroke-linejoin="round"/></svg></div>
    <p class="perk-text">5-year money back guarantee on wallet</p>
  </div>
  <div class="perk" style="left:492px">
    <div class="perk-badge"><svg width="90" height="90" viewBox="0 0 90 90"><circle cx="45" cy="45" r="40" fill="#fff"/><circle cx="45" cy="45" r="28" fill="none" stroke="#f0a020" stroke-width="4"/><text x="45" y="52" text-anchor="middle" font-family="Fredoka, sans-serif" font-weight="700" font-size="20" fill="#f0a020">100%</text></svg></div>
    <p class="perk-text">High quality and durable leather</p>
  </div>
  <div class="perk" style="left:729px">
    <div class="perk-badge"><svg width="90" height="80" viewBox="0 0 90 80"><rect x="12" y="18" width="66" height="46" rx="6" fill="#fff"/><rect x="12" y="28" width="66" height="8" fill="#e9771b"/><rect x="52" y="42" width="20" height="14" rx="3" fill="#e9771b"/></svg></div>
    <p class="perk-text">Edit any of our ready made wallet designs</p>
  </div>
  <div class="perk" style="left:966px">
    <div class="perk-badge"><svg width="90" height="80" viewBox="0 0 90 80"><path d="M45 8c-22 0-38 14-38 32s16 32 34 32c6 0 6-6 3-10s0-9 6-9h10c14 0 22-8 22-18C82 20 66 8 45 8z" fill="#fff"/><circle cx="28" cy="32" r="5" fill="#e9771b"/><circle cx="44" cy="22" r="5" fill="#e9771b"/><circle cx="62" cy="28" r="5" fill="#e9771b"/></svg></div>
    <p class="perk-text">Customize your own wallet design</p>
  </div>
</section>

<section class="features">
  <h2 class="section-title">Wallet Features</h2>
  <div class="feature-wallet abs" role="img" aria-label="Black printed wallet on a white paint splash"></div>
  <div class="spec" style="left:170px;top:246px"><span class="spec-dot" style="background:var(--violet)"></span>Reinforced Corners</div>
  <div class="spec" style="left:170px;top:328px"><span class="spec-dot" style="background:var(--teal)"></span>Durable Luxury<br>Leather</div>
  <div class="spec" style="left:170px;top:404px"><span class="spec-dot" style="background:var(--green)"></span>Slim Design - 15mm<br>Thick</div>
  <div class="spec right" style="right:166px;top:246px"><span class="spec-dot" style="background:var(--yellow)"></span>Two Note Pockets</div>
  <div class="spec right" style="right:166px;top:330px"><span class="spec-dot" style="background:var(--orange)"></span>Two Coin<br>Compartments</div>
  <div class="spec right" style="right:166px;top:400px"><span class="spec-dot" style="background:var(--magenta)"></span>Six Credit Card Slots</div>
</section>
<div class="detail" style="left:139px;border-color:var(--violet)" role="img" aria-label="Close-up of wallet corner stitching"></div>
<div class="detail" style="left:300px;border-color:var(--teal)" role="img" aria-label="Close-up of leather texture"></div>
<div class="detail" style="left:460px;border-color:var(--green)" role="img" aria-label="Side view showing slim profile"></div>
<div class="detail" style="left:621px;border-color:var(--yellow)" role="img" aria-label="Hand opening the note pockets"></div>
<div class="detail" style="left:778px;border-color:var(--orange)" role="img" aria-label="Coin compartment detail"></div>
<div class="detail" style="left:936px;border-color:var(--magenta)" role="img" aria-label="Credit card slots detail"></div>

<section class="products">
  <h2 class="section-title">Our Products</h2>
  <p class="products-intro">Lorem Ipsum is simply dummy text of the printing and typesetting industry. Lorem Ipsum has been the industry's standard dummy text ever since the 1500s.</p>
  <div class="product" style="left:141px">
    <div class="product-shot" role="img" aria-label="Wallet on a black and white paisley pattern" style="background:linear-gradient(135deg,#e6e6e6,#3a3a3a 50%,#d0d0d0)"></div>
    <p class="product-name">Product 1</p><p class="product-price">$109</p>
  </div>
  <div class="product" style="left:461px">
    <div class="product-shot" role="img" aria-label="Wallet on an orange and cream texture" style="background:linear-gradient(135deg,#f7c65a,#e0471b 50%,#fbe7a6)"></div>
    <p class="product-name">Product 2</p><p class="product-price">$119</p>
  </div>
  <div class="product" style="left:782px">
    <div class="product-shot" role="img" aria-label="Wallet on blue denim" style="background:linear-gradient(135deg,#4a6fa5,#2a3f66 50%,#5b7fb5)"></div>
    <p class="product-name">Product 3</p><p class="product-price">$129</p>
  </div>
  <a class="btn">View All</a>
</section>

<section class="templates">
  <div class="media templates-screen" role="img" aria-label="Pre-made templates page with wallet designs"></div>
  <h2 class="title">Edit Templates</h2>
  <div class="copy">
    <p>With over 20 pre-made templates available, you can edit it whatever wallet style you want.</p>
    <p>It's easy as A-B-C!</p>
  </div>
  <a class="btn">Get Started</a>
</section>

<section class="customize">
  <h2 class="title">Customize Your Own Template</h2>
  <div class="copy">
    <p>Expand your horizon and be creative!</p>
    <p>Upload a photo you want for your wallet design and preview the 3D model of your artwork.</p>
  </div>
  <a class="btn">Try It Now</a>
  <div class="media customize-screen" role="img" aria-label="Customize page showing a wallet with a red patterned design"></div>
</section>

<footer class="site-footer"></footer>

</body>
</html>
```